Plotvane Caribbean

We need a vibrant, user friendly and exciting website for our land search company called "plotVane" This application will help individuals locate and or list lots for sale within the Caribbean. We will offer a small cash back incentive to buyers that purchase land from our site, and we will charge a 1%-2% success fee to our sellers once a successful transaction is made. We would like to become a match making site, matching buyers and sellers on our platform. We will also include a service directory and marketing advertisement spot for other service providers for a fee. We would like to see a webdesign incorporating Caribbean colors (blue, green and yellow) with very modern clean lines, very picturesque and easy to use.

Industry/Entity Type

Real Estate

Coding

Number of Pages Required

5+ page

Font styles to use
Sans Serif

Colors
ffffff
85acd3
b768aa
dbdbdb

Requirements
Nice to have
• Scenic photos of the ocean and beautiful landscape

```html
<!DOCTYPE html>
<html lang="en">
<head>
<meta charset="utf-8">
<title>Plotvane Caribbean</title>
<link href="https://fonts.googleapis.com/css2?family=Open+Sans:ital,wght@0,400;0,600;0,700;1,600&family=Roboto+Condensed:wght@700&display=swap" rel="stylesheet">
<style>
:root{
  --blue:#2e8ff0;
  --ink:#2b2b2b;
  --text:#444;
  --frame:#e4e4e4;
  --paper:#ffffff;
  --mist:#f3f3f3;
  --rule:#c8c8c8;
}
*{margin:0;padding:0;box-sizing:border-box}
html,body{width:754px;height:1200px;overflow:hidden;background:var(--frame)}
body{font-family:"Open Sans",Arial,sans-serif;color:var(--text);position:relative}
.page{position:absolute;left:9px;top:9px;width:736px;height:1182px;background:var(--paper);overflow:hidden}
.abs{position:absolute}

/* header */
.info-tab{left:412px;top:0;width:312px;height:23px;}
.info-tab svg{position:absolute;left:0;top:0}
.info-text{left:444px;top:4px;font:700 9.5px "Open Sans",sans-serif;color:#fff;display:flex;align-items:center;gap:5px;letter-spacing:.1px}
.social{left:640px;top:4px;display:flex;gap:3px}
.social span{width:14px;height:14px;border:1.2px solid #fff;border-radius:50%}
.brand{left:19px;top:31px;font:600 22px "Open Sans",sans-serif;color:var(--blue);letter-spacing:.5px}
.nav{left:345px;top:60px;display:flex;align-items:center;gap:12px;font:700 10px "Roboto Condensed",sans-serif;color:var(--ink)}
.nav a{color:inherit;text-decoration:none;padding:3px 1px}
.nav .current{border-bottom:2.5px solid var(--blue)}
.nav .cta{background:var(--blue);color:#fff;padding:5px 8px;border-radius:2px}

/* hero */
.hero{left:0;top:81px;width:736px;height:348px;background:linear-gradient(180deg,#3b9fe0 0%,#6cc3ea 40%,#4ab0dc 58%,#1f7fb8 75%,#2d6d92 100%)}
.tagline{left:0;top:429px;width:736px;height:68px;background:linear-gradient(180deg,#d9d9d9,#eeeeee 50%,#dcdcdc);box-shadow:0 8px 10px -6px rgba(0,0,0,.35);display:flex;align-items:center;justify-content:center;font:700 18px "Open Sans",sans-serif;color:var(--ink)}
.accent{color:var(--blue)}

/* sections */
.section-title{display:flex;align-items:center;justify-content:center;gap:14px;font:700 15px "Open Sans",sans-serif;color:var(--ink);width:736px;left:0}
.section-title::before,.section-title::after{content:"";width:58px;height:1px;background:var(--rule)}
.about-title{top:535px}
.about-copy{left:45px;top:580px;width:646px;text-align:center;font-size:8.2px;line-height:12.5px;color:#3c3c3c}
.testimonials{left:0;top:677px;width:736px;height:259px;background:var(--mist)}
.testi-title{top:38px}
.quote{left:136px;top:90px;width:500px;font-size:8.2px;line-height:11.3px;color:#3c3c3c}
.qmark{font:700 28px Georgia,serif;color:var(--ink);line-height:1}
.q-open{left:110px;top:88px}
.q-close{left:534px;top:122px}
.author{left:136px;top:150px;font:italic 600 10.5px "Open Sans",sans-serif;color:var(--ink)}
.dots{left:349px;top:193px;display:flex;gap:3px}
.dots span{width:7.5px;height:7.5px;border-radius:50%;border:1px solid #555}
.dots .on{background:var(--blue);border-color:var(--blue)}

/* footer */
.footer{left:0;top:927px;width:736px;height:232px}
.footer-logo{left:0;top:28px;width:736px;text-align:center;font:600 20px "Open Sans",sans-serif;color:var(--blue);letter-spacing:.5px}
.col h4{font:700 10.5px "Open Sans",sans-serif;color:var(--ink);padding-bottom:5px;border-bottom:1px solid #bdbdbd;width:86px;margin-bottom:10px}
.col ul{list-style:none;font:600 8px "Open Sans",sans-serif;letter-spacing:.8px;color:var(--ink);line-height:11.6px}
.col-nav{left:70px;top:92px}
.col-company{left:220px;top:92px}
.col-info{left:341px;top:92px}
.reserve{left:495px;top:93px;width:172px;height:119px;background:var(--blue);border:1.5px solid #fff;border-radius:3px;color:#fff;text-align:center;padding-top:9px}
.reserve .label{font:700 9.5px "Open Sans",sans-serif}
.reserve .phone{font:700 15.5px "Open Sans",sans-serif;display:flex;align-items:center;justify-content:center;gap:4px;margin-top:2px}
.reserve .addr{font-size:9.5px;line-height:12px;margin-top:19px}
.copyright{left:0;top:1159px;width:736px;height:23px;background:var(--paper);text-align:center;font:700 7px "Open Sans",sans-serif;color:var(--ink);padding-top:6px}
</style>
</head>
<body>
<div class="page">
  <header>
    <div class="abs info-tab">
      <svg width="312" height="23" viewBox="0 0 312 23"><polygon points="0,0 312,0 291,23 22,23" fill="#2e8ff0"/></svg>
    </div>
    <div class="abs info-text">
      <svg width="14" height="14" viewBox="0 0 24 24"><circle cx="12" cy="12" r="10.5" fill="none" stroke="#fff" stroke-width="2"/><path d="M8.5 6.5l2 2.6-1.3 1.4c.7 1.6 1.9 2.8 3.4 3.5l1.4-1.3 2.6 2-1 1.8c-3.8-.3-7.6-4-8-7.9z" fill="#fff"/></svg>
      FOR INFORMATION : 123-456-7890
    </div>
    <div class="abs social" aria-label="Social links"><span></span><span></span><span></span></div>
    <div class="abs brand">Plotvane Caribbean</div>
    <nav class="abs nav">
      <a class="current" href="#">HOME</a>
      <a href="#">WHO WE ARE</a>
      <a href="#">OUR SERVICES</a>
      <a href="#">WHY PLOTVANE</a>
      <a href="#">CONTACT</a>
      <a class="cta" href="#">SEARCH LAND</a>
    </nav>
  </header>

  <div class="abs hero" role="img" aria-label="Scenic photo of a lantern-lit wooden pier leading to thatched huts over calm blue Caribbean water at dusk"></div>
  <div class="abs tagline">THE LEADER FOR&nbsp;<span class="accent">LAND SEARCH IN</span>&nbsp;CARIBBEAN</div>

  <h2 class="abs section-title about-title"><span>WHO <span class="accent">WE ARE</span></span></h2>
  <p class="abs about-copy">Lorem ipsum dolor sit amet, consectetuer adipiscing elit, sed diam nonummy nibh euismod tincidunt ut laoreet dolore magna aliquam erat volutpat. Ut wisi enim ad minim veniam, quis nostrud exerci tation ullamcorper suscipit lobortis nisl ut aliquip ex ea commodo consequat. Duis autem vel eum iriure dolor in hendrerit in vulputate velit esse molestie consequat, vel illum dolore eu feugiat nulla facilisis at vero eros et accumsan et iusto odio dignissim qui blandit praesent luptatum zzril delenit augue duis dolore te feugait nulla facilisi. Nam liber tempor cum soluta nobis eleifend option congue nihil imperdiet doming id quod mazim placerat facer possim assum. Typi non habent claritatem insitam; est usus legentis in iis qui facit eorum claritatem. Investigationes demonstraverunt lectores legere me lius quod ii legunt saepius.</p>

  <section class="abs testimonials">
    <h2 class="abs section-title testi-title">TESTIMONIALS</h2>
    <div class="abs qmark q-open">&#8221;</div>
    <p class="abs quote">Lorem ipsum dolor sit amet, consectetuer adipiscing elit, sed diam nonummy nibh euismod tincidunt ut laoreet dolore magna aliquam erat volutpat. Ut wisi enim ad minim veniam, quis nostrud exerci tation ullamcorper suscipit lobortis nisl ut aliquip ex ea commodo feugait nulla facilisi. Nam liber tempor cum soluta nobis eleifend option congue nihil imperdiet doming id quod mazim placerat facer possim assum. Typi non habent claritatem insitam; est usus legentis in iis qui facit eorum claritatem.</p>
    <div class="abs qmark q-close">&#8221;</div>
    <div class="abs author">Marisol Fenwick</div>
    <div class="abs dots"><span class="on"></span><span></span><span></span><span></span></div>
  </section>

  <footer class="abs footer">
    <svg class="abs" style="left:0;top:0" width="736" height="232" viewBox="0 0 736 232">
      <defs><linearGradient id="footFade" x1="0" y1="0" x2="0" y2="1"><stop offset="0" stop-color="#f1f1f1"/><stop offset="1" stop-color="#c9c9c9"/></linearGradient></defs>
      <path d="M0 9H255L270 0H466L481 9H736V232H0Z" fill="url(#footFade)"/>
    </svg>
    <div class="abs footer-logo">Plotvane Caribbean</div>
    <div class="abs col col-nav"><h4>Navigation</h4><ul><li>Home</li><li>Who We Are</li><li>Our Services</li><li>Why Plotvane</li><li>Contact</li><li>Search Land</li></ul></div>
    <div class="abs col col-company"><h4>Company</h4><ul><li>About</li><li>Testimonials</li><li>Contact</li></ul></div>
    <div class="abs col col-info"><h4>Information</h4><ul><li>FAQs</li><li>Privacy Policy</li><li>Terms &amp; Conditions</li></ul></div>
    <div class="abs reserve">
      <div class="label">FOR RESERVATION</div>
      <div class="phone">
        <svg width="21" height="21" viewBox="0 0 24 24"><circle cx="12" cy="12" r="10.5" fill="none" stroke="#fff" stroke-width="1.8"/><path d="M8.5 6.5l2 2.6-1.3 1.4c.7 1.6 1.9 2.8 3.4 3.5l1.4-1.3 2.6 2-1 1.8c-3.8-.3-7.6-4-8-7.9z" fill="#fff"/></svg>
        (123) 456-7890
      </div>
      <div class="addr">123 Lorem Ipsum Dr<br>Suite 123<br>Caribbean</div>
    </div>
  </footer>
  <div class="abs copyright">© 2017 PLOTVANE CARIBBEAN I ALL RIGHTS RESERVED</div>
</div>
</body>
</html>
```